The design should be a multi-page, foldable flyer with the logo and the product name on the front and the web address on the back.
DoLMUO is a word play on "zebra", which the design should reflect in some way.

Target Market(s)

Schools and individual teachers

Industry/Entity Type

Product

Colors
ffffff
000000

```html
<!DOCTYPE html>
<html lang="en">
<head>
<meta charset="utf-8">
<title>DoLMUO Flyer Spread</title>
<link rel="stylesheet" href="https://fonts.googleapis.com/css2?family=Open+Sans:wght@400;600;700;800&display=swap">
<style>
  :root{
    --stage:#2a2a2b;
    --paper:#ffffff;
    --ink:#000000;
    --silver-light:#d9d9db;
    --silver:#b9b9bc;
    --band-dark:#3b3b3d;
    --band-mid:#58585b;
    --band-deep:#2f2f31;
    --text-dark:#2b2b2b;
    --text-light:#f2f2f2;
    --text-muted:#cfcfd2;
  }
  *{box-sizing:border-box;margin:0;padding:0}
  html,body{width:1200px;height:789px;overflow:hidden}
  body{background:var(--stage);font-family:"Open Sans",Arial,sans-serif;position:relative}
  .spread{position:absolute;left:105px;top:44px;width:990px;height:700px;display:flex;box-shadow:0 10px 30px rgba(0,0,0,.5)}
  .page{position:relative;width:495px;height:700px;overflow:hidden;background:var(--paper)}
  .page-art{position:absolute;inset:0}
  /* back page */
  .about{position:absolute;left:28px;top:36px;width:440px;color:var(--text-dark)}
  .about-title{font-size:17px;font-weight:400;letter-spacing:.5px;padding-bottom:6px;border-bottom:1px solid #8d8d90;width:230px}
  .about-title strong{font-weight:700}
  .about-text{margin-top:8px;font-size:9.5px;line-height:1.35}
  .brand{position:absolute;display:flex;align-items:center;gap:8px;color:var(--text-dark);font-weight:600}
  .brand-mark{width:14px;height:14px;border-radius:50%;background:var(--ink)}
  .brand--back{left:24px;top:560px;font-size:20px}
  .contact{position:absolute;left:290px;top:566px;width:180px;color:var(--text-light);text-align:right}
  .contact-title{font-size:15px;font-weight:700;letter-spacing:.5px;padding-bottom:5px;border-bottom:1px solid var(--text-muted)}
  .contact-list{list-style:none;margin-top:6px;font-size:9.5px;line-height:1.6}
  .contact-list li{display:flex;justify-content:flex-end;align-items:center;gap:5px}
  .contact-list svg{width:9px;height:9px;fill:var(--text-muted);flex:none}
  .web--back{position:absolute;left:24px;top:676px;font-size:10px;color:var(--text-light)}
  /* front page */
  .brand--front{left:30px;top:42px;font-size:28px}
  .cover-title{position:absolute;right:36px;top:430px;text-align:right;color:var(--text-light)}
  .cover-title h1{font-size:32px;font-weight:800;color:var(--paper)}
  .cover-title p{font-size:19px;line-height:1.25;margin-top:4px}
  .web-bar{position:absolute;left:120px;right:0;top:604px;height:40px;background:var(--band-deep);display:flex;align-items:center;justify-content:center;color:var(--text-light);font-size:14px;letter-spacing:.3px}
</style>
</head>
<body>
<main class="spread">
  <section class="page page--back">
    <svg class="page-art" width="495" height="700" viewBox="0 0 495 700">
      <defs>
        <linearGradient id="backTop" x1="0" y1="0" x2="0" y2="1">
          <stop offset="0" stop-color="#cfcfd1"/><stop offset="1" stop-color="#b4b4b8"/>
        </linearGradient>
        <linearGradient id="backPhoto" x1="0" y1="0" x2="1" y2="1">
          <stop offset="0" stop-color="#9da3a8"/><stop offset=".45" stop-color="#b89678"/><stop offset="1" stop-color="#7f8f9c"/>
        </linearGradient>
        <linearGradient id="darkBand" x1="0" y1="0" x2="1" y2="1">
          <stop offset="0" stop-color="var(--band-mid)"/><stop offset="1" stop-color="var(--band-dark)"/>
        </linearGradient>
      </defs>
      <rect width="495" height="175" fill="url(#backTop)"/>
      <polygon points="0,175 495,175 495,420 0,540" fill="url(#backPhoto)" role="img" aria-label="Photo of smiling students writing at desks in a library"/>
      <polygon points="0,540 495,420 495,470 0,700" fill="var(--silver-light)"/>
      <polygon points="0,675 495,470 495,700 0,700" fill="url(#darkBand)"/>
    </svg>
    <div class="about">
      <h2 class="about-title">ABOUT <strong>DoLMUO</strong></h2>
      <p class="about-text">Lorem ipsum dolor sit amet, consectetur adipiscing elit, sed do eiusmod tempor incididunt ut labore et dolore magna aliqua. Ut enim ad minim veniam, quis nostrud exercitation ullamco laboris nisi ut aliquip ex ea commodo consequat. Duis aute irure dolor in reprehenderit in voluptate velit esse cillum dolore eu fugiat nulla pariatur. Excepteur sint occaecat cupidatat non proident, sunt in culpa qui officia deserunt mollit anim id est laborum.</p>
    </div>
    <div class="brand brand--back"><span class="brand-mark"></span>DoLMUO</div>
    <div class="contact">
      <h3 class="contact-title">CONTACT DETAILS</h3>
      <ul class="contact-list">
        <li><svg viewBox="0 0 10 10"><path d="M5 0a3.5 3.5 0 0 0-3.5 3.5C1.5 6 5 10 5 10s3.5-4 3.5-6.5A3.5 3.5 0 0 0 5 0zm0 5a1.5 1.5 0 1 1 0-3 1.5 1.5 0 0 1 0 3z"/></svg>Address line 1, Address line 1</li>
        <li>Address line 2, Address line 2</li>
        <li><svg viewBox="0 0 10 10"><path d="M2 1l2 2-1 1.2a6 6 0 0 0 2.8 2.8L7 6l2 2-1.2 1.5C4 9 1 6 .5 2.2z"/></svg>0123 456 789</li>
        <li><svg viewBox="0 0 10 10"><path d="M0 2h10v6H0zM0 2l5 3.5L10 2" stroke="#3b3b3d" stroke-width=".8"/></svg>info@example.com</li>
      </ul>
    </div>
    <p class="web--back">www.yourwebsite.com</p>
  </section>

  <section class="page page--front">
    <svg class="page-art" width="495" height="700" viewBox="0 0 495 700">
      <defs>
        <linearGradient id="frontPhoto" x1="0" y1="0" x2="1" y2="1">
          <stop offset="0" stop-color="#e9e2d6"/><stop offset=".5" stop-color="#d8b796"/><stop offset="1" stop-color="#c9ccc8"/>
        </linearGradient>
        <linearGradient id="frontBand" x1="0" y1="0" x2="1" y2="1">
          <stop offset="0" stop-color="var(--band-mid)"/><stop offset="1" stop-color="var(--band-dark)"/>
        </linearGradient>
      </defs>
      <polygon points="0,0 495,0 495,380 0,470" fill="url(#frontPhoto)" role="img" aria-label="Photo of a hand filling in a multiple-choice answer sheet with a pencil"/>
      <polygon points="0,470 495,380 495,398 0,488" fill="var(--silver)"/>
      <polygon points="0,488 495,398 495,700 0,700" fill="url(#frontBand)"/>
    </svg>
    <div class="brand brand--front"><span class="brand-mark"></span>DoLMUO</div>
    <div class="cover-title">
      <h1>DoLMUO</h1>
      <p>Draft Organize Learn Mark Update<br>&amp; Oversee</p>
    </div>
    <div class="web-bar">www.yourwebsite.com</div>
  </section>
</main>
</body>
</html>
```